Business Card Design, including supply of raw art files plus a vector diagram of the flenzo logo and

We need the business card design for a company that is launching a new exciting product. The brief requires the submission of the following once the final design is chosen:

- business card layout including raw files
- a composite vector image file of the flenzo logo and tag line
- a standalone vector image file of the flenzo logo

The product will be launched as a customer engagement app.

It has 4 core modules which enables a person to do multiple things - book tours and activities, order takeaways, search for local deals and offers. A universal currency is at the heart of this product. When you use the app, you earn cashback rewards when shopping or buying at any of the merchant partners across the modules as . These rewards can then be used as full or part payment when buying goods or services at these merchant partners.

The business card must help us build the brand, communicate the benefit of the brand's key focus - the ability to earn and burn this universal cashback ccurrency - across the 4 modules - booking of tours and activities, ordering, searching for local deals and payment.

We would like the design to use the brand's blue colour the hex colour is: 00
Dark grey : 646464
Darker blue shadow: 058bdd
Main Blue: 0084ff

We need to translate this into a CMYK print or spot colour print.

Both print options to be supplied as separate files.

An example of the base concept we have in mind is attached for your reference.

The font used by the brand is Proxima Nova.

Industry/Entity Type

Business

Contact Information for Business Card

Carla Whitfield
Marketing
W: www.flenzo.co
M: + 61 407318265
T: +61 2 9375 4120
A: Suite 7, Level 2, 14-18 Harrow Lane, Sydney, NSW, 2000, Australia

Font styles to use
Sans Serif

Requirements
Must have
• flEnzo logo and tagline
• address details
• flEnzo icons as supplied
Nice to have
• would like to have the option of a spot varnish layer over the logo and icons at the back of the card

```html
<!DOCTYPE html>
<html lang="en">
<head>
<meta charset="utf-8">
<title>flenzo Business Card</title>
<link rel="stylesheet" href="https://fonts.googleapis.com/css2?family=Open+Sans:wght@400;600;700&display=swap">
<style>
  :root {
    --brand-blue: #0084ff;
    --sky-blue: #1aa6ee;
    --deep-blue: #058bdd;
    --name-blue: #12a0dc;
    --dark-grey: #646464;
    --ink: #2f2f2f;
    --card-face: #f4f5f6;
    --backdrop: #dde1e4;
    --white: #ffffff;
  }
  * { box-sizing: border-box; margin: 0; padding: 0; }
  html, body {
    width: 1200px;
    height: 900px;
    overflow: hidden;
  }
  body {
    background: var(--backdrop);
    font-family: "Open Sans", sans-serif;
    position: relative;
  }
  .business-card {
    position: absolute;
    left: 145px;
    top: 172px;
    width: 910px;
    height: 557px;
    border-radius: 26px;
    background: linear-gradient(180deg, #fbfbfb 0%, var(--card-face) 100%);
    box-shadow: 0 18px 40px rgba(0,0,0,0.12);
    overflow: hidden;
  }
  .brand-lockup {
    position: absolute;
    left: 0;
    top: 36px;
    width: 100%;
    text-align: center;
  }
  .brand-name {
    font-size: 92px;
    font-weight: 400;
    line-height: 1.05;
    color: var(--dark-grey);
    letter-spacing: 2px;
  }
  .brand-tagline {
    margin-top: 6px;
    font-size: 26px;
    font-weight: 400;
    color: var(--dark-grey);
    letter-spacing: 4px;
    text-transform: uppercase;
  }
  .contact {
    position: absolute;
    left: 0;
    width: 100%;
    text-align: center;
  }
  .contact-name {
    top: 245px;
    font-size: 29px;
    font-weight: 700;
    color: var(--name-blue);
    letter-spacing: 0.5px;
  }
  .contact-role {
    top: 284px;
    font-size: 24px;
    color: var(--ink);
  }
  .contact-lines {
    top: 335px;
    font-size: 23px;
    color: var(--ink);
  }
  .contact-lines .label {
    color: var(--brand-blue);
    font-weight: 700;
  }
  .contact-lines .web { color: var(--brand-blue); }
  .contact-lines .divider { margin: 0 8px; }
  .contact-address {
    top: 383px;
    font-size: 23px;
    color: var(--ink);
  }
  .module-band {
    position: absolute;
    left: 0;
    bottom: 0;
    width: 100%;
    height: 112px;
    background: linear-gradient(90deg, #2aaaf0 0%, var(--sky-blue) 55%, var(--deep-blue) 100%);
  }
  .module {
    position: absolute;
    top: 20px;
    width: 160px;
    margin-left: -80px;
    text-align: center;
    color: var(--white);
    font-size: 24px;
  }
  .module svg {
    display: block;
    margin: 0 auto 2px;
    width: 48px;
    height: 44px;
  }
</style>
</head>
<body>
  <main class="business-card">
    <div class="brand-lockup">
      <div class="brand-name">flenzo</div>
      <div class="brand-tagline">rewards that travel</div>
    </div>

    <h1 class="contact contact-name">CARLA WHITFIELD</h1>
    <p class="contact contact-role">Marketing</p>
    <p class="contact contact-lines">
      <span class="label">M:</span> + 61 407318265<span class="divider">|</span><span class="label">P:</span> +61 2 9375 4120<span class="divider">|</span><span class="web">www.flenzo.co</span>
    </p>
    <p class="contact contact-address">Suite 7, Level 2, 14-18 Harrow Lane, Sydney, NSW, 2000, Australia</p>

    <footer class="module-band">
      <div class="module" style="left:182px">
        <svg viewBox="0 0 48 44" aria-hidden="true">
          <path d="M4 12h10l4-6h12l4 6h10v26H4z" fill="#fff"/>
          <circle cx="24" cy="24" r="9" fill="#1aa6ee"/>
          <circle cx="24" cy="24" r="6" fill="#fff"/>
        </svg>
        Camera
      </div>
      <div class="module" style="left:357px">
        <svg viewBox="0 0 48 44" aria-hidden="true">
          <path d="M10 14a14 14 0 0 1 22-8" stroke="#fff" stroke-width="4" fill="none"/>
          <path d="M30 1l6 6-8 3z" fill="#fff"/>
          <path d="M38 30a14 14 0 0 1-22 8" stroke="#fff" stroke-width="4" fill="none"/>
          <path d="M18 43l-6-6 8-3z" fill="#fff"/>
          <circle cx="24" cy="22" r="9" fill="#fff"/>
          <text x="24" y="27" font-size="13" font-weight="700" text-anchor="middle" fill="#1aa6ee" font-family="Open Sans, sans-serif">$</text>
        </svg>
        Cash back
      </div>
      <div class="module" style="left:570px">
        <svg viewBox="0 0 48 44" aria-hidden="true">
          <path d="M12 40L32 12" stroke="#fff" stroke-width="3.5" stroke-linecap="round"/>
          <ellipse cx="35" cy="8" rx="5" ry="7" transform="rotate(35 35 8)" fill="#fff"/>
          <path d="M36 40L16 14" stroke="#fff" stroke-width="3.5" stroke-linecap="round"/>
          <path d="M10 4l6 10M14 2l5 10M18 0l4 10" stroke="#fff" stroke-width="2.5" stroke-linecap="round"/>
        </svg>
        Cutlery
      </div>
      <div class="module" style="left:749px">
        <svg viewBox="0 0 48 44" aria-hidden="true">
          <path d="M28 2h16v16L22 40 6 24z" fill="#fff"/>
          <circle cx="37" cy="9" r="3.5" fill="#1aa6ee"/>
        </svg>
        Tag
      </div>
    </footer>
  </main>
</body>
</html>
```